Web Button design and production

I need remote control like buttons (or your own design of buttons if I like it)
3x4 text buttons (normal, pressed, disabled)
3x1 empty button (normal, pressed, disabled)
3x6 buttons with glyph (normal, pressed, disabled)
3x288 with 24h time "00:00", "00:05", "00:10" (normal, pressed, disabled)
4 LED (red, green, orange, black)
I will upload the background image as soon as possible (black plastic)
See attached images
Q: Do the buttons have to be gray/black?
A: It should look like a high end remote control. It could be brushed aluminum as well, or something you come up with. But I guess black or dark grey would be best. The background will be picsharbor 40561739, but it's not available yet.
Q: Do I have to provide all buttons for the contest?
A: No! I only need one button (3 states) and a LED to decide. Only the winner will do the whole job.
Q: Is the Designer who wins the contest expected to complete all the extra buttons?
A: Yes, please.
Plastic

```html
<!DOCTYPE html>
<html lang="en">
<head>
<meta charset="utf-8">
<title>Button States Kit</title>
<link rel="stylesheet" href="https://fonts.googleapis.com/css2?family=Arimo:wght@400&family=Nothing+You+Could+Do&display=swap">
<style>
  :root {
    --page: #eeeeed;
    --rule: #a9a9a9;
    --ink: #4e4e4e;
    --icon: #505050;
    --face-top: #f6f6f6;
    --face-bottom: #dedede;
    --edge: #b9b9b9;
    --lip: #9d9d9d;
    --red-top: #f7a0a3;
    --red-bottom: #ef6f75;
    --red-edge: #c9545a;
    --red-flat: #f26a70;
    --green-top: #cbe28e;
    --green-bottom: #a8cc5c;
    --green-edge: #7f9f3e;
    --green-flat: #a6ca5d;
    --blue-top: #b3e6fb;
    --blue-bottom: #7fcdf1;
    --blue-edge: #5aa3c6;
    --blue-flat: #7cd0f4;
  }
  html, body { margin: 0; padding: 0; overflow: hidden; }
  body { width: 1200px; height: 540px; background: var(--page); position: relative; font-family: "Arimo", Arial, sans-serif; }

  .state-label {
    position: absolute; top: 10px; width: 140px; text-align: center;
    font-family: "Nothing You Could Do", cursive; font-size: 24px; color: #222; letter-spacing: 1px;
  }
  .divider { position: absolute; top: 8px; height: 524px; border-left: 1px dotted var(--rule); }

  .btn {
    position: absolute; box-sizing: border-box; display: flex; align-items: center; justify-content: center;
    text-align: center; color: var(--ink); line-height: 1.15;
    border: 1px solid var(--edge); border-radius: 5px;
    background: linear-gradient(var(--face-top), var(--face-bottom));
    box-shadow: inset 0 1px 0 #fff, 0 3px 0 var(--lip), 0 5px 6px rgba(0,0,0,.22);
  }
  .btn.is-hover { background: linear-gradient(#eeeeee, #d8d8d8); }
  .btn.is-active {
    background: linear-gradient(#e2e2e2, #e9e9e9);
    box-shadow: inset 0 1px 3px rgba(0,0,0,.12);
    border-color: #c3c3c3;
  }
  .btn svg { fill: var(--icon); }

  .text-sm { font-size: 21px; }
  .text-md { font-size: 27px; }
  .text-lg { font-size: 27px; }

  .swatch { position: absolute; width: 48px; height: 44px; box-sizing: border-box; border-radius: 5px; }
  .swatch.red { background: linear-gradient(var(--red-top), var(--red-bottom)); border: 1px solid var(--red-edge); box-shadow: 0 3px 0 #b9474d, 0 5px 6px rgba(0,0,0,.2); }
  .swatch.green { background: linear-gradient(var(--green-top), var(--green-bottom)); border: 1px solid var(--green-edge); box-shadow: 0 3px 0 #728f38, 0 5px 6px rgba(0,0,0,.2); }
  .swatch.blue { background: linear-gradient(var(--blue-top), var(--blue-bottom)); border: 1px solid var(--blue-edge); box-shadow: 0 3px 0 #4d90b0, 0 5px 6px rgba(0,0,0,.2); }
  .swatch.is-hover.red { background: linear-gradient(#f59599, #ee6a70); }
  .swatch.is-hover.green { background: linear-gradient(#c3dc82, #a2c656); }
  .swatch.is-hover.blue { background: linear-gradient(#a8e1f9, #76c8ee); }
  .swatch.is-active { box-shadow: inset 0 1px 3px rgba(0,0,0,.15); }
  .swatch.is-active.red { background: var(--red-flat); }
  .swatch.is-active.green { background: var(--green-flat); }
  .swatch.is-active.blue { background: var(--blue-flat); }

  .btn.red { background: linear-gradient(var(--red-top), var(--red-bottom)); border-color: var(--red-edge); box-shadow: inset 0 1px 0 rgba(255,255,255,.5), 0 3px 0 #b9474d, 0 5px 6px rgba(0,0,0,.2); }
  .btn.green { background: linear-gradient(var(--green-top), var(--green-bottom)); border-color: var(--green-edge); box-shadow: inset 0 1px 0 rgba(255,255,255,.5), 0 3px 0 #728f38, 0 5px 6px rgba(0,0,0,.2); }
  .btn.blue { background: linear-gradient(var(--blue-top), var(--blue-bottom)); border-color: var(--blue-edge); box-shadow: inset 0 1px 0 rgba(255,255,255,.5), 0 3px 0 #4d90b0, 0 5px 6px rgba(0,0,0,.2); }
  .btn.red svg { fill: #b8343b; stroke: #b8343b; }
  .btn.green svg { fill: none; stroke: #5f8a1f; }
  .btn.blue svg { fill: #2f8fbd; }
</style>
</head>
<body>

  <!-- state columns -->
  <div class="state-label" style="left:178px">LINK</div>
  <div class="state-label" style="left:358px">HOVER</div>
  <div class="state-label" style="left:536px">ACTIVE</div>

  <div class="divider" style="left:342px"></div>
  <div class="divider" style="left:522px"></div>
  <div class="divider" style="left:730px"></div>

  <!-- link state -->
  <div class="btn text-sm" style="left:200px;top:62px;width:96px;height:53px">Login</div>
  <div class="btn text-md" style="left:200px;top:142px;width:96px;height:53px">00:00</div>
  <div class="btn text-lg" style="left:179px;top:220px;width:144px;height:90px">Book<br>Now</div>
  <div class="swatch red" style="left:224px;top:331px"></div>
  <div class="swatch green" style="left:224px;top:398px"></div>
  <div class="swatch blue" style="left:224px;top:473px"></div>

  <!-- hover state -->
  <div class="btn text-sm is-hover" style="left:380px;top:62px;width:96px;height:53px">Login</div>
  <div class="btn text-md is-hover" style="left:380px;top:142px;width:96px;height:53px">00:00</div>
  <div class="btn text-lg is-hover" style="left:361px;top:220px;width:144px;height:90px">Book<br>Now</div>
  <div class="swatch red is-hover" style="left:404px;top:331px"></div>
  <div class="swatch green is-hover" style="left:404px;top:398px"></div>
  <div class="swatch blue is-hover" style="left:404px;top:473px"></div>

  <!-- active state -->
  <div class="btn text-sm is-active" style="left:558px;top:62px;width:96px;height:53px">Login</div>
  <div class="btn text-md is-active" style="left:558px;top:142px;width:96px;height:53px">00:00</div>
  <div class="btn text-lg is-active" style="left:539px;top:220px;width:144px;height:90px">Book<br>Now</div>
  <div class="swatch red is-active" style="left:586px;top:331px"></div>
  <div class="swatch green is-active" style="left:586px;top:398px"></div>
  <div class="swatch blue is-active" style="left:586px;top:473px"></div>

  <!-- remote glyph buttons -->
  <div class="btn" style="left:778px;top:36px;width:96px;height:54px" aria-label="Back">
    <svg width="32" height="20" viewBox="0 0 32 20"><path d="M0 10 L11 0 V6 H32 V14 H11 V20 Z"/></svg>
  </div>
  <div class="btn" style="left:898px;top:36px;width:96px;height:54px" aria-label="Return">
    <svg width="26" height="24" viewBox="0 0 26 24"><path d="M0 8 L10 0 V5 H26 V12 H14 V24 H8 V12 H10 V16 Z"/></svg>
  </div>

  <div class="btn" style="left:778px;top:110px;width:96px;height:91px" aria-label="Previous">
    <svg width="24" height="26" viewBox="0 0 24 26"><path d="M0 13 L24 0 V26 Z"/></svg>
  </div>
  <div class="btn" style="left:900px;top:110px;width:96px;height:91px" aria-label="Next">
    <svg width="24" height="26" viewBox="0 0 24 26"><path d="M24 13 L0 0 V26 Z"/></svg>
  </div>

  <div class="btn" style="left:778px;top:222px;width:96px;height:56px" aria-label="Skip back">
    <svg width="30" height="20" viewBox="0 0 30 20"><rect x="0" y="0" width="5" height="20"/><path d="M7 10 L30 0 V20 Z"/></svg>
  </div>
  <div class="btn" style="left:900px;top:222px;width:96px;height:56px" aria-label="Skip forward">
    <svg width="30" height="20" viewBox="0 0 30 20"><path d="M23 10 L0 0 V20 Z"/><rect x="25" y="0" width="5" height="20"/></svg>
  </div>

  <div class="btn red" style="left:778px;top:300px;width:48px;height:46px" aria-label="Power">
    <svg width="22" height="22" viewBox="0 0 22 22"><path d="M6.5 5.5 A8 8 0 1 0 15.5 5.5" fill="none" stroke-width="2.4"/><line x1="11" y1="1" x2="11" y2="11" stroke-width="2.4"/></svg>
  </div>
  <div class="btn red" style="left:834px;top:300px;width:48px;height:46px" aria-label="Record">
    <svg width="18" height="18" viewBox="0 0 18 18"><circle cx="9" cy="9" r="9" stroke="none"/></svg>
  </div>
  <div class="btn green" style="left:890px;top:300px;width:48px;height:46px" aria-label="Down">
    <svg width="24" height="22" viewBox="0 0 24 22"><path d="M2 2 L12 20 L22 2" stroke-width="2.6"/></svg>
  </div>
  <div class="btn green" style="left:948px;top:300px;width:48px;height:46px" aria-label="Up">
    <svg width="24" height="22" viewBox="0 0 24 22"><path d="M2 20 L12 2 L22 20" stroke-width="2.6"/></svg>
  </div>

  <div class="btn blue" style="left:778px;top:372px;width:70px;height:48px" aria-label="Rewind">
    <svg width="30" height="16" viewBox="0 0 30 16"><path d="M0 8 L15 0 V16 Z M15 8 L30 0 V16 Z"/></svg>
  </div>
  <div class="btn" style="left:865px;top:372px;width:48px;height:48px" aria-label="Play">
    <svg width="18" height="18" viewBox="0 0 18 18"><path d="M18 9 L0 0 V18 Z"/></svg>
  </div>
  <div class="btn blue" style="left:926px;top:372px;width:70px;height:48px" aria-label="Fast forward">
    <svg width="30" height="16" viewBox="0 0 30 16"><path d="M15 8 L0 0 V16 Z M30 8 L15 0 V16 Z"/></svg>
  </div>

  <div class="btn" style="left:778px;top:446px;width:48px;height:46px" aria-label="Stop">
    <svg width="14" height="14" viewBox="0 0 14 14"><rect width="14" height="14" rx="2"/></svg>
  </div>
  <div class="btn" style="left:835px;top:446px;width:70px;height:46px" aria-label="Pause or play">
    <svg width="42" height="20" viewBox="0 0 42 20"><rect x="0" y="1" width="4" height="18"/><rect x="7" y="1" width="4" height="18"/><path d="M13 20 L19 0 H21 L15 20 Z"/><path d="M42 10 L24 1 V19 Z"/></svg>
  </div>

</body>
</html>
```